Tin Lantern "Cold Harbor" New Single Cover

Create cover artwork for the band Tin Lantern' new single "Cold Harbor" being released early 2020. Style, font and graphics to be consistent with band's previous releases and overall brand identity. Visit www.tinlanternband.example and our Spotify page https://listen.tunevault.example/artist/8QXzrT4LmNbW2cPd7KeYjA?si=HVkR3sTpZ9wLqYb2nMcXuE to view our previous releases and overall brand identity. Some examples attached as well. We are looking for someone to work with on future projects as well.

Lyrics are here: https://pages.draftbox.example/document/d/7KpRw2mXn_9LqTe4Zs8Vd_HyjB2cF5t03Qa71nRkwLpY/edit

Music is here: https://wavecrate.example/tinlantern/cold-harbor/s-rbmtx

Font styles to use
Sans Serif

Colors

Designer to choose colors to be used in the design.

Requirements
Must have
• Must be consistent with current brand identity and with prior album / single art.

```html
<!DOCTYPE html>
<html lang="en">
<head>
<meta charset="utf-8">
<title>Tin Lantern — Cold Harbor</title>
<link rel="stylesheet" href="https://fonts.googleapis.com/css2?family=Josefin+Sans:wght@100;200;600&display=swap">
<style>
  :root {
    --plum: #5b2d7b;
    --rose: #d8708f;
    --brick-light: #82297f;
    --brick-deep: #682d80;
  }
  html, body {
    margin: 0;
    padding: 0;
    overflow: hidden;
    background: var(--plum);
  }
  .cover {
    position: relative;
    width: 1200px;
    height: 1200px;
    background: var(--plum);
    overflow: hidden;
  }
  .cover-frame {
    position: absolute;
    left: 53px;
    top: 53px;
    width: 1094px;
    height: 1094px;
    border: 3px solid var(--rose);
    box-sizing: border-box;
  }
  .single-title {
    position: absolute;
    top: 138px;
    left: 0;
    width: 100%;
    margin: 0;
    text-align: center;
    font-family: "Josefin Sans", sans-serif;
    font-weight: 100;
    font-size: 104px;
    line-height: 1;
    letter-spacing: 0.12em;
    padding-left: 0.12em;
    box-sizing: border-box;
    color: var(--rose);
  }
  .brick-emblem {
    position: absolute;
    left: 345px;
    top: 342px;
    width: 510px;
    height: 510px;
  }
  .band-name {
    position: absolute;
    top: 962px;
    left: 0;
    width: 100%;
    margin: 0;
    text-align: center;
    font-family: "Josefin Sans", sans-serif;
    font-weight: 600;
    font-size: 60px;
    line-height: 1;
    letter-spacing: 0.08em;
    padding-left: 0.08em;
    box-sizing: border-box;
    color: var(--rose);
  }
</style>
</head>
<body>
  <main class="cover">
    <div class="cover-frame"></div>
    <h1 class="single-title">COLD HARBOR</h1>
    <svg class="brick-emblem" viewBox="0 0 510 510" role="img" aria-label="Round emblem of a stacked brick wall in magenta tones">
      <defs>
        <linearGradient id="brick-glow" x1="0.2" y1="0.15" x2="0.85" y2="0.9">
          <stop offset="0" stop-color="var(--brick-light)"/>
          <stop offset="1" stop-color="var(--brick-deep)"/>
        </linearGradient>
      </defs>
      <circle cx="255" cy="255" r="255" fill="url(#brick-glow)"/>
    </svg>
    <h2 class="band-name">TIN LANTERN</h2>
  </main>
</body>
</html>
```